Sumworks.co.uk - front page and content page design
Site design for Sumworks.co.uk - a UK site hosting different calculators
Creative Brief
Internet Services
http://www.plotmeadow.co.uk
Project: Sumworks.co.uk
Idea: To host all of the different types of calculators on the site with supporting content
Our idea is generating targeted traffic through generic domains (we've got 4,500!). With Sumworks.co.uk, the domain will host loads of different calculators with content supporting the calculators on offer.
For Sumworks.co.uk, we'd like a design that is clean but colourful and allows us to colour the different sections of the site that we'll have. The initial premise is that we'll have sections for the different 'types' of calculators:
Health calculators
Finance calculators
Maths calculators
Conversion calculators
Pregnancy calculators
Within each section will be different calculators - so, for example, in Health, there will be a BMI calculator, BMR calculator and so on.
Ideally, we'd like each 'section' to have a different colour - i.e. blue for Health, green for Finance, blue for Maths, etc. The colours can be chosen by the designer as to what looks best.
We'd like a front page design and also a content page design. The home page shouldn't be too different in structure/layout to the content pages (i.e. structure follows through).
Ideally, there will be a column on the right hand side that allows advertising (300 x 250) and the main column for content should be at least 540px (this is where content and weidgets/calculators will be placed).
Once in a section, there should be a left menu that allows users to choose the type of calculator they want within that section.
This is our first try on Pixelgrove and we're hoping that if this works out, we can find some designer(s) through this who we can offer many more design projects as we have many generic domain names waiting to be designed.
Likes: Clean, colourful, elegant, professional
www.vitalpage.com
http://www.brightjotapp.com/tour/why-use-brightjot
http://www.kelvo.com/

```html
<!DOCTYPE html>
<html lang="en">
<head>
<meta charset="utf-8">
<title>Sumworks.co.uk – Mortgage calculator</title>
<link rel="stylesheet" href="https://fonts.googleapis.com/css2?family=Arimo:wght@400;700&display=swap">
<style>
:root{
  --page:#e4e4e4;
  --header-top:#d2d2d2;
  --header-bottom:#f4f4f4;
  --white:#ffffff;
  --text:#333333;
  --muted:#666666;
  --tab:#4a4a4a;
  --tab-dark:#2f2f2f;
  --orange:#f5a200;
  --orange-dark:#e08a00;
  --blue:#1b8fd0;
  --blue-light:#5fb7e8;
  --menu:#ececec;
  --line:#d6d6d6;
  --ad:#c9c9c9;
  --ad-text:#8a8a8a;
  --footer-line:#333333;
}
*{box-sizing:border-box;margin:0;padding:0}
html,body{width:1200px;height:571px;overflow:hidden}
body{font-family:"Arimo",Arial,sans-serif;background:var(--page);color:var(--text);position:relative}
.header{position:absolute;left:0;top:0;width:1200px;height:96px;background:linear-gradient(var(--header-top),var(--header-bottom))}
.brand{position:absolute;left:264px;top:14px;display:flex;align-items:center;gap:10px}
.brand-dot{width:34px;height:34px;border-radius:50%;background:var(--orange)}
.brand-name{color:var(--white);font-size:34px;font-weight:700;letter-spacing:-.5px}
.search{position:absolute;left:800px;top:21px;display:flex;gap:5px}
.search-field{width:112px;height:15px;background:var(--white);border:1px solid #aaa;font-size:9px;color:#999;padding:2px 4px}
.search-go{width:34px;height:15px;background:var(--orange);font-size:9px;font-weight:700;text-align:center;line-height:15px;color:#333}
.tabs{position:absolute;left:398px;top:55px;display:flex;gap:12px}
.tab{width:101px;height:27px;background:linear-gradient(var(--tab),var(--tab-dark));color:var(--white);font-size:14px;text-align:center;line-height:27px}
.tab.active{background:linear-gradient(#ffbb33,var(--orange))}
.sidebar{position:absolute;left:247px;top:106px;width:156px}
.sidebar h2{font-size:13px;font-weight:700;height:22px;line-height:22px}
.menu{background:var(--menu);height:284px;list-style:none}
.menu>li{font-size:12px;font-weight:700;height:32px;line-height:32px;padding-left:10px;border-bottom:1px solid var(--white)}
.menu>li.active{background:linear-gradient(90deg,var(--blue),var(--blue-light));color:var(--white)}
.submenu{list-style:none;background:var(--white)}
.submenu li{font-size:10px;height:30px;line-height:30px;padding-left:18px;color:var(--muted)}
.submenu li::before{content:"";display:inline-block;width:6px;height:6px;border:1px solid #999;border-radius:50%;margin-right:8px;vertical-align:middle}
.submenu li.current{color:var(--blue);text-decoration:underline}
.content{position:absolute;left:403px;top:125px;width:329px;height:288px;background:var(--white);border:1px solid var(--line);padding:12px 20px}
.content h1{font-size:10px;color:var(--blue);font-weight:700;padding-bottom:8px;border-bottom:1px solid var(--line)}
.form{margin-top:44px;font-size:8px}
.row{display:flex;align-items:center;gap:6px;height:18px}
.row label{width:74px}
.field{display:inline-block;height:12px;border:1px solid #bbb;background:var(--white)}
.row.total{font-weight:700;margin-top:2px}
.intro{position:absolute;left:20px;top:206px;width:280px;font-size:9px;line-height:12px}
.calc-btn{position:absolute;right:6px;bottom:10px;width:72px;height:22px;border-radius:3px;background:linear-gradient(#ffbb33,var(--orange-dark));font-size:10px;font-weight:700;text-align:center;line-height:22px;color:#333}
.ad{position:absolute;left:749px;width:218px;background:var(--ad);color:var(--ad-text);font-size:15px;font-weight:700;display:flex;align-items:center;justify-content:center;border:1px solid #bbb}
.ad.one{top:120px;height:173px}
.ad.two{top:312px;height:178px}
.footer{position:absolute;left:247px;top:503px;width:720px;border-top:3px solid var(--footer-line)}
.social{position:absolute;left:7px;top:9px;display:flex;gap:4px}
.social span{width:16px;height:16px;border-radius:3px}
.footer-links{position:absolute;left:212px;top:6px;display:flex;list-style:none;font-size:9px;font-weight:700}
.footer-links li{padding:0 11px;border-right:1px solid #999}
.footer-links li:last-child{border-right:0}
.copyright{position:absolute;left:0;top:52px;width:720px;text-align:center;font-size:9px}
</style>
</head>
<body>
<header class="header">
  <div class="brand"><span class="brand-dot"></span><span class="brand-name">Sumworks.co.uk</span></div>
  <div class="search"><span class="search-field">Search site</span><span class="search-go">GO</span></div>
  <nav class="tabs">
    <span class="tab">Health</span>
    <span class="tab active">Finance</span>
    <span class="tab">Maths</span>
    <span class="tab">Conversion</span>
    <span class="tab">Pregnancy</span>
  </nav>
</header>

<aside class="sidebar">
  <h2>Calculators</h2>
  <ul class="menu">
    <li>Health</li>
    <li class="active">Finance</li>
    <li style="padding:0;height:auto;border:0">
      <ul class="submenu">
        <li class="current">Mortgage calculator</li>
        <li>Calculator - 2</li>
        <li>Calculator - 3</li>
        <li>Calculator - 4</li>
      </ul>
    </li>
    <li>Maths</li>
    <li>Conversion</li>
    <li>Pregnancy</li>
  </ul>
</aside>

<main class="content">
  <h1>Mortgage calculator</h1>
  <div class="form">
    <div class="row"><label>Mortgage amount</label>£ <span class="field" style="width:46px"></span></div>
    <div class="row"><label>Mortgage term</label><span class="field" style="width:40px"></span> years or <span class="field" style="width:40px"></span> months</div>
    <div class="row"><label>Interest rate</label><span class="field" style="width:60px"></span> % per year</div>
    <div class="row"><label>Mortgage start date</label><span class="field" style="width:30px"></span><span class="field" style="width:30px"></span><span class="field" style="width:36px"></span></div>
    <div class="row total"><label>Monthly Payments:</label></div>
  </div>
  <p class="intro">Lorem ipsum dolor sit amet, consectetuer adipiscing elit, sed diam nonummy nibh euismod tincidunt ut laoreet dolore magna aliquam erat volutpat.</p>
  <span class="calc-btn">Calculate</span>
</main>

<div class="ad one">ad space</div>
<div class="ad two">ad space</div>

<footer class="footer">
  <div class="social">
    <span style="background:#3b5998"></span>
    <span style="background:#4aa8e0"></span>
    <span style="background:#f28a1e"></span>
  </div>
  <ul class="footer-links">
    <li>Home</li><li>About Us</li><li>Contact Us</li><li>Help</li><li>F.A.Q.</li>
  </ul>
  <p class="copyright">© Sumworks.co.uk. All Rights Reserved.</p>
</footer>
</body>
</html>
```